Discreet simple classy for adult entertainment

I would like a matte black business card with gold writing for my business. Keeping it simple. Having my following:

Lana frost
Events. Entertainment. Promotions
0491726580

or alternatively could have what i had on my previous card below but i think i prefer the above as again - discretion.

Maybe a nice gold line thru the card or some other very simple design . Or not open to ideas/ can be doublesided if any good ideas with that.

included pics of my old bus card. not sure weather i want a photo on it or not. if i do it wont be the same pic. i kinda wanted a card that was discreet so if it was in someones wallet they wouldn't neccessarily realise it was from a stripper.

Target Market(s)

men

Industry/Entity Type

Business

Contact Information for Business Card

Lana frost
0491726580

Requirements
Nice to have
• i don't know i am really open to anything. im giving my cards to guys so something they can have in their wallet that is discreet preferably.

```html
<!DOCTYPE html>
<html lang="en">
<head>
<meta charset="utf-8">
<title>Lana frost — Business Card</title>
<link rel="stylesheet" href="https://fonts.googleapis.com/css2?family=Titan+One&family=Source+Sans+3:wght@400&display=swap">
<style>
  :root {
    --card-black: #000000;
    --gold: #c9b100;
    --smoke-deep: #3a3300;
    --smoke-soft: #1c1900;
  }
  html, body {
    margin: 0;
    padding: 0;
    width: 1200px;
    height: 800px;
    overflow: hidden;
    background: var(--card-black);
  }
  .card {
    position: relative;
    width: 1200px;
    height: 800px;
    background: var(--card-black);
    overflow: hidden;
  }
  .smoke-backdrop {
    position: absolute;
    inset: 0;
    width: 1200px;
    height: 800px;
  }
  .gold-rule {
    position: absolute;
    left: 271px;
    top: 0;
    width: 19px;
    height: 244px;
    background: var(--gold);
  }
  .identity {
    position: absolute;
    left: 271px;
    top: 206px;
    margin: 0;
    color: var(--gold);
  }
  .identity__name {
    margin: 0;
    font-family: "Titan One", "Arial Black", sans-serif;
    font-weight: 400;
    font-size: 42px;
    line-height: 50px;
    letter-spacing: 1px;
    word-spacing: 10px;
  }
  .identity__services {
    list-style: none;
    margin: 0;
    padding: 0;
    font-family: "Source Sans 3", "Helvetica Neue", sans-serif;
    font-weight: 400;
    font-size: 44px;
    line-height: 56px;
  }
  .identity__phone {
    margin: 0;
    font-family: "Titan One", "Arial Black", sans-serif;
    font-weight: 400;
    font-size: 40px;
    line-height: 56px;
    letter-spacing: 1px;
  }
</style>
</head>
<body>
  <div class="card">
    <svg class="smoke-backdrop" viewBox="0 0 1200 800" role="img" aria-label="Faint flowing gold smoke wisps sweeping across the black card">
      <defs>
        <radialGradient id="smoke-upper" cx="0.55" cy="0.3" r="0.55">
          <stop offset="0" stop-color="var(--smoke-soft)" stop-opacity="0.2"/>
          <stop offset="0.7" stop-color="var(--smoke-deep)" stop-opacity="0.45"/>
          <stop offset="1" stop-color="var(--card-black)" stop-opacity="0"/>
        </radialGradient>
        <radialGradient id="smoke-lower" cx="0.5" cy="0.75" r="0.5">
          <stop offset="0" stop-color="var(--smoke-deep)" stop-opacity="0.5"/>
          <stop offset="1" stop-color="var(--card-black)" stop-opacity="0"/>
        </radialGradient>
      </defs>
      <rect width="1200" height="800" fill="url(#smoke-upper)"/>
      <rect width="1200" height="800" fill="url(#smoke-lower)"/>
    </svg>

    <div class="gold-rule"></div>

    <div class="identity">
      <h1 class="identity__name">Lana frost</h1>
      <ul class="identity__services">
        <li>Events</li>
        <li>Entertainment</li>
        <li>Promotions</li>
      </ul>
      <p class="identity__phone">0491726580</p>
    </div>
  </div>
</body>
</html>
```